Business Card Design

We Need a business card design for my company based in Tv Radio and music Productions and hunt Talent.

Industry/Entity Type

Business

Contact Information for Business Card

BrivaTune Production's, Renzo Bettafiore,Cell Phone 427 5139048
Musician, Productor, Hunt Talent. Miami Fla. www.brivatune.net Mail. renzobettafiore@kovamail.com

```html
<!DOCTYPE html>
<html lang="en">
<head>
<meta charset="utf-8">
<title>BrivaTune Productions – Business Card</title>
<link rel="stylesheet" href="https://fonts.googleapis.com/css2?family=Oswald:wght@400;500;600&display=swap">
<style>
  :root {
    --backdrop: #2b2b2b;
    --card: #f6f6f6;
    --ink: #111111;
    --yellow: #f8d53a;
    --purple-light: #8c5cae;
    --purple-dark: #673c90;
    --purple-text: #6a3d9c;
    --brand-red: #b3372a;
  }
  * { margin: 0; padding: 0; box-sizing: border-box; }
  html, body { width: 1200px; height: 1000px; overflow: hidden; }
  body {
    background: var(--backdrop);
    font-family: "Oswald", "Arial Narrow", sans-serif;
    color: var(--ink);
    position: relative;
  }
  .card { position: absolute; background: var(--card); overflow: hidden; }

  /* Front */
  .card-front { left: 75px; top: 32px; width: 498px; height: 830px; }
  .brand-mark {
    position: absolute;
    display: flex; align-items: center; gap: 14px;
  }
  .brand-mark .dot { border-radius: 50%; background: var(--yellow); flex: none; }
  .brand-mark .name { color: var(--brand-red); font-weight: 600; line-height: 1; }
  .card-front .brand-mark { left: 95px; top: 230px; }
  .card-front .brand-mark .dot { width: 90px; height: 90px; }
  .card-front .brand-mark .name { font-size: 58px; }

  .roles { position: absolute; left: 0; top: 481px; list-style: none; }
  .role {
    width: 393px; height: 52px; margin-bottom: 22px;
    background: linear-gradient(180deg, var(--purple-dark) 0%, var(--purple-light) 45%, var(--purple-light) 60%, var(--purple-dark) 100%);
    text-align: right; padding-right: 27px;
    font-size: 33px; font-weight: 500; line-height: 52px;
  }

  /* Back */
  .card-back { left: 638px; top: 130px; width: 502px; height: 837px; }
  .stripe { position: absolute; left: 0; width: 55px; background: var(--yellow); }
  .stripe-top { top: 0; height: 494px; }
  .stripe-bottom { top: 755px; height: 82px; }
  .name-band {
    position: absolute; left: 185px; top: 125px; width: 317px; height: 60px;
    background: var(--yellow);
    padding-left: 22px;
    font-size: 36px; font-weight: 600; line-height: 60px;
  }
  .company {
    position: absolute; left: 89px; top: 283px;
    font-size: 37px; font-weight: 500; line-height: 1.2;
  }
  .contact { position: absolute; left: 60px; top: 345px; }
  .contact-row { display: flex; align-items: baseline; height: 47px; }
  .contact-row dt {
    width: 99px; text-align: right; padding-right: 14px;
    font-size: 22px; font-weight: 500;
  }
  .contact-row dd { color: var(--purple-text); font-size: 25px; font-weight: 500; }
  .contact-row dd.email { font-size: 23px; }
  .card-back .brand-mark { left: 215px; top: 620px; }
  .card-back .brand-mark .dot { width: 56px; height: 56px; }
  .card-back .brand-mark .name { font-size: 40px; }
</style>
</head>
<body>
  <section class="card card-front" aria-label="Card front">
    <div class="brand-mark">
      <span class="dot"></span>
      <span class="name">BrivaTune</span>
    </div>
    <ul class="roles">
      <li class="role">Musician</li>
      <li class="role">Productor</li>
      <li class="role">Hunt Talent</li>
      <li class="role">Miami Fla</li>
    </ul>
  </section>

  <section class="card card-back" aria-label="Card back">
    <div class="stripe stripe-top"></div>
    <div class="stripe stripe-bottom"></div>
    <h1 class="name-band">Renzo Bettafiore</h1>
    <h2 class="company">BrivaTune Productions</h2>
    <dl class="contact">
      <div class="contact-row"><dt>Mobile:</dt><dd>427 5139048</dd></div>
      <div class="contact-row"><dt>Email:</dt><dd class="email">renzobettafiore@kovamail.com</dd></div>
      <div class="contact-row"><dt>Web:</dt><dd>www.brivatune.net</dd></div>
    </dl>
    <div class="brand-mark">
      <span class="dot"></span>
      <span class="name">BrivaTune</span>
    </div>
  </section>
</body>
</html>
```